Business Card Design

I have two logos , one is for the front of the card and the other for the back. The front image is the road and the sun, the back image should be the atom with the motto at the bottom. The back of the card should be black with the atom and lettering white. The front should have the image with the road and lettering black with the yellow sun all on a white background.
Updates

I have changed what I would like done. The only logo I want to use is the atom logo. White lettering with a black background on the front and back of the card. There should be no contact info on the back of the card. On the back there should b the logo with company name and the slogan underneath at the bottom of the card, also on the back if you can have the logo  image in the background as well in a gray or silver can be tiled or cascade of some sort.

On the front it should have all of the contact info with an email address added  tidewaveprints@fernmail.net   Black background with white lettering and another larger image of the logo in a gray or silver in the background. The logo and name side by side with the slogan directly under the name.

Industry/Entity Type

Business

Contact Information for Business Card

Colin Marsh
Director of Operations
6182 Hollis Ln #517
Georgetown, TX 78415
Cell: (512)487-3056
Fax: (512)871-4402

```html
<!DOCTYPE html>
<html lang="en">
<head>
<meta charset="utf-8">
<title>Prairie Mobile Imaging – Business Card</title>
<link rel="stylesheet" href="https://fonts.googleapis.com/css2?family=Tinos&family=Open+Sans:wght@400&family=Questrial&display=swap">
<style>
  :root {
    --stage-center: #5c5c5c;
    --stage-edge: #050505;
    --card-black: #0b0b0b;
    --text-light: #f2f2f2;
    --text-soft: #d4d4d4;
    --silver: #9a9a9a;
    --blue-deep: #12304a;
    --blue-mid: #1f6b8f;
    --grey-light: #8a8a8a;
    --grey-dark: #1a1a1a;
    --back-center: #666666;
    --back-edge: #2e2e2e;
    --white: #ffffff;
  }
  * { margin: 0; padding: 0; box-sizing: border-box; }
  html, body { width: 1200px; height: 999px; overflow: hidden; }
  body {
    position: relative;
    background: radial-gradient(ellipse 70% 65% at 50% 50%, var(--stage-center) 0%, #3a3a3a 55%, var(--stage-edge) 100%);
  }
  .card { position: absolute; width: 725px; height: 414px; overflow: hidden; }

  /* Front */
  .card-front { left: 126px; top: 62px; background: var(--card-black); }
  .card-front .swoosh { position: absolute; inset: 0; }
  .brand-name {
    position: absolute; inset: 0;
    font-family: "Tinos", serif;
    color: var(--text-light);
    font-weight: 400;
  }
  .brand-name .line-1 { position: absolute; left: 34px; top: 128px; font-size: 31px; white-space: nowrap; }
  .brand-name .line-2 { position: absolute; left: 122px; top: 170px; font-size: 25px; white-space: nowrap; }
  .brand-slogan {
    position: absolute; left: 36px; top: 210px;
    font-family: "Open Sans", sans-serif; font-size: 14px; letter-spacing: 0.4px;
    color: var(--silver); white-space: nowrap;
  }
  .brand-dot {
    position: absolute; left: 268px; top: 146px;
    width: 44px; height: 44px; border-radius: 50%;
    background: var(--silver);
  }
  .divider { position: absolute; left: 405px; top: 96px; }
  .person-name {
    position: absolute; left: 446px; top: 88px;
    font-family: "Tinos", serif; font-size: 32px; color: var(--text-light);
  }
  .person-title {
    position: absolute; left: 447px; top: 126px;
    font-family: "Open Sans", sans-serif; font-size: 17px; color: var(--text-soft);
  }
  .contact {
    position: absolute; left: 443px;
    font-family: "Open Sans", sans-serif; font-size: 17px; line-height: 24px; color: var(--text-soft);
    display: flex; align-items: flex-start; gap: 8px; white-space: nowrap;
  }
  .contact svg { flex: none; margin-top: 5px; }
  .contact-address { top: 186px; }
  .contact-cell { top: 242px; }
  .contact-fax { top: 266px; }
  .contact-email { top: 290px; font-size: 15px; }

  /* Back */
  .card-back {
    left: 281px; top: 522px;
    background: radial-gradient(ellipse 75% 70% at 50% 50%, var(--back-center) 0%, #555 50%, var(--back-edge) 100%);
  }
  .back-dot {
    position: absolute; left: 174px; top: 145px;
    width: 18px; height: 18px; border-radius: 50%; background: var(--white);
  }
  .back-name {
    position: absolute; left: 236px; top: 182px;
    font-family: "Questrial", sans-serif; font-size: 41px; letter-spacing: -0.5px;
    color: var(--white); white-space: nowrap;
  }
  .back-slogan {
    position: absolute; left: 0; right: 0; bottom: 34px; text-align: center;
    font-family: "Questrial", sans-serif; font-size: 18px; letter-spacing: 1px;
    color: var(--white); white-space: nowrap;
  }
</style>
</head>
<body>

<section class="card card-front" aria-label="Business card front">
  <svg class="swoosh" width="725" height="414" viewBox="0 0 725 414" aria-hidden="true">
    <defs>
      <linearGradient id="blueBand" x1="0" y1="0" x2="1" y2="0">
        <stop offset="0" stop-color="var(--blue-deep)"/>
        <stop offset="0.35" stop-color="var(--blue-mid)"/>
        <stop offset="1" stop-color="var(--blue-deep)"/>
      </linearGradient>
      <linearGradient id="greyBand" x1="0" y1="0" x2="0" y2="1">
        <stop offset="0" stop-color="var(--grey-light)"/>
        <stop offset="1" stop-color="var(--grey-dark)"/>
      </linearGradient>
    </defs>
    <path d="M0,279 C130,352 320,378 604,358" fill="none" stroke="var(--blue-mid)" stroke-width="3"/>
    <path d="M0,292 C140,362 330,386 604,358 C530,385 480,398 446,414 L0,414 Z" fill="url(#blueBand)"/>
    <path d="M452,414 C560,372 660,344 725,306 L725,414 Z" fill="url(#greyBand)"/>
    <path d="M440,414 C556,370 656,342 725,304" fill="none" stroke="var(--white)" stroke-width="4"/>
  </svg>

  <div class="brand-name">
    <span class="line-1">Prairie Mobile</span>
    <span class="line-2">Imaging</span>
  </div>
  <div class="brand-slogan">Imaging that comes to you</div>
  <span class="brand-dot" aria-hidden="true"></span>

  <svg class="divider" width="6" height="214" viewBox="0 0 6 214" aria-hidden="true">
    <path d="M3,0 C5,70 5,144 3,214 C1,144 1,70 3,0 Z" fill="var(--silver)"/>
  </svg>

  <div class="person-name">Colin Marsh</div>
  <div class="person-title">Director of Operations</div>

  <div class="contact contact-address">
    <svg width="17" height="17" viewBox="0 0 16 16" aria-hidden="true">
      <circle cx="8" cy="8" r="7" fill="var(--text-light)"/>
      <g fill="none" stroke="var(--card-black)" stroke-width="1">
        <ellipse cx="8" cy="8" rx="3" ry="7"/>
        <line x1="1" y1="8" x2="15" y2="8"/>
        <line x1="2.5" y1="4.5" x2="13.5" y2="4.5"/>
        <line x1="2.5" y1="11.5" x2="13.5" y2="11.5"/>
      </g>
    </svg>
    <span>6182 Hollis Ln #517<br>Georgetown, TX 78415</span>
  </div>
  <div class="contact contact-cell">
    <svg width="17" height="17" viewBox="0 0 16 16" aria-hidden="true">
      <rect x="1.5" y="0.5" width="13" height="15" rx="2" fill="var(--text-light)"/>
      <rect x="3.5" y="2.5" width="9" height="11" fill="var(--card-black)"/>
      <line x1="4.5" y1="12" x2="11.5" y2="4" stroke="var(--text-light)" stroke-width="1.3"/>
    </svg>
    <span>Cell: (512)487-3056</span>
  </div>
  <div class="contact contact-fax">
    <svg width="17" height="17" viewBox="0 0 18 16" aria-hidden="true">
      <rect x="4" y="0" width="8" height="6" fill="var(--text-light)"/>
      <rect x="0" y="7" width="18" height="6" fill="var(--text-light)"/>
      <rect x="2" y="13" width="14" height="3" fill="var(--text-light)"/>
      <rect x="5" y="8.5" width="8" height="1.5" fill="var(--card-black)"/>
    </svg>
    <span>Fax: (512)871-4402</span>
  </div>
  <div class="contact contact-email">
    <svg width="17" height="17" viewBox="0 0 16 16" aria-hidden="true">
      <rect x="0.5" y="3" width="15" height="10" rx="1" fill="var(--text-light)"/>
      <path d="M1,3.5 L8,9 L15,3.5" fill="none" stroke="var(--card-black)" stroke-width="1.2"/>
    </svg>
    <span>tidewaveprints@fernmail.net</span>
  </div>
</section>

<section class="card card-back" aria-label="Business card back">
  <span class="back-dot" aria-hidden="true"></span>
  <div class="back-name">Prairie Mobile Imaging</div>
  <div class="back-slogan">Imaging that comes to you</div>
</section>

</body>
</html>
```